Professional services business card

This is for a new business in New Zealand, providing professional advice to boards of directors of companies
The point of difference is a strong blend of Financial and IT knowledge

Target audience are senior business executives, CEO/CFO/President, etc.
So, simple but appealing
Business colours are orange and blue

Sample logo attached
proposed Content also attached - feedback on wording is welcome
Updates

Please provide for a logo to be added - about 30 mm wide and 10 mm high

the company name is "Corvel Waypoint Ltd" - logo now uploaded to the project brief

Information to include are now in the second file that was uploaded

Industry/Entity Type

Business

```html
<!DOCTYPE html>
<html lang="en">
<head>
<meta charset="utf-8">
<title>Corvel Waypoint – Business Card</title>
<link rel="stylesheet" href="https://fonts.googleapis.com/css2?family=Noto+Sans:wght@400;700&family=PT+Sans:wght@400;700&display=swap">
<style>
  :root {
    --backdrop: #435256;
    --page: #ffffff;
    --card: #ffffff;
    --brand-blue: #33aaff;
    --logo-blue: #29a9ee;
    --brand-orange: #f99b40;
    --ink: #000000;
    --card-edge: #c9d0d2;
  }
  * { box-sizing: border-box; margin: 0; padding: 0; }
  html, body {
    width: 1200px;
    height: 672px;
    overflow: hidden;
    background: var(--page);
  }
  .stage {
    position: relative;
    width: 1317px;
    height: 740px;
    transform: scale(0.9112);
    transform-origin: 0 0;
    background: var(--page);
  }
  .backdrop {
    position: absolute;
    left: 0; top: 0;
    width: 1317px;
    height: 520px;
    background: var(--backdrop);
  }
  .card {
    position: absolute;
    top: 114px;
    width: 502px;
    height: 325px;
    background: var(--card);
    outline: 1px solid var(--card-edge);
    overflow: hidden;
  }
  .card--front { left: 116px; }
  .card--back { left: 695px; }
  .card__face {
    position: absolute;
    inset: 0;
  }
  .card--back .card__face { transform: rotate(180deg); }
  .swoosh {
    position: absolute;
    inset: 0;
    width: 502px;
    height: 325px;
  }
  .swoosh__field { fill: var(--brand-blue); }
  .swoosh__band {
    fill: none;
    stroke: var(--brand-orange);
    stroke-width: 40;
  }
  .wordmark {
    position: absolute;
    left: 36px;
    top: 150px;
    width: 180px;
    font-family: "Noto Sans", sans-serif;
    font-weight: 700;
    font-size: 21px;
    line-height: 1.15;
    color: var(--logo-blue);
    text-align: center;
    letter-spacing: 0.2px;
  }
  .contact {
    position: absolute;
    left: 277px;
    top: 50px;
    font-family: "Noto Sans", sans-serif;
    color: var(--ink);
    font-size: 14px;
    line-height: 17.5px;
  }
  .contact__name {
    font-size: 23px;
    font-weight: 700;
    line-height: 28px;
  }
  .contact__block { margin-top: 17px; }
  .contact__label { font-weight: 700; }
  .contact__web {
    margin-top: 26px;
    font-size: 9px;
    line-height: 13px;
  }
  .services {
    position: absolute;
    left: 248px;
    top: 108px;
    font-family: "PT Sans", sans-serif;
    color: var(--ink);
    font-size: 13.5px;
  }
  .services__title {
    font-weight: 700;
    font-size: 14.5px;
    margin-bottom: 24px;
  }
  .services__list {
    list-style: disc;
    padding-left: 18px;
    line-height: 26px;
  }
</style>
</head>
<body>
  <main class="stage">
    <div class="backdrop"></div>

    <section class="card card--front" aria-label="Business card front">
      <div class="card__face">
        <svg class="swoosh" viewBox="0 0 502 325" aria-hidden="true">
          <path class="swoosh__field" d="M170 0 H502 V325 H362 C352 190 152 120 152 22 Q152 0 170 0 Z"/>
          <path class="swoosh__band" d="M112 -5 C104 100 318 150 332 330"/>
        </svg>
        <div class="wordmark">Corvel Waypoint</div>
        <div class="contact">
          <p class="contact__name">Mara Kettle</p>
          <p>M.Com, ACA(NZ), ACMA</p>
          <div class="contact__block">
            <p>Corvel Waypoint Ltd</p>
            <p>PO Box 40917</p>
            <p>Harbour Quay</p>
            <p>&nbsp;Wellington 5010</p>
          </div>
          <p class="contact__block"><span class="contact__label">Phone:</span> 021 555 0148</p>
          <div class="contact__web">
            <p>E: Mara.Kettle@corvelway.nz</p>
            <p>www.linkedin.com/in/marakettle</p>
          </div>
        </div>
      </div>
    </section>

    <section class="card card--back" aria-label="Business card back">
      <div class="card__face">
        <svg class="swoosh" viewBox="0 0 502 325" aria-hidden="true">
          <path class="swoosh__field" d="M170 0 H502 V325 H362 C352 190 152 120 152 22 Q152 0 170 0 Z"/>
          <path class="swoosh__band" d="M112 -5 C104 100 318 150 332 330"/>
        </svg>
        <div class="wordmark">Corvel Waypoint</div>
        <div class="services">
          <p class="services__title">Talk to us about</p>
          <ul class="services__list">
            <li>Governance</li>
            <li>Good Stewardship</li>
            <li>Financial Insight</li>
            <li>Information Technology Insight</li>
            <li>Mentoring and Business Advice</li>
          </ul>
        </div>
      </div>
    </section>
  </main>
</body>
</html>
```